詳細はzipファイルにまとめておりおますので、こちらからダウンロードしてください。

http://3.hakobuya.nu/0522-k83920fa17de462093b8e1c7f06a35d9

【デザインの参考サイト】
クライアント様からは、以下の参考サイトを挙げていただいております。
http://plumtivra.com/
https://sorvik4417.com/

ただし、上記サイトはおしゃれではあるものの、少しアピールが弱いようにも思います。
最終的な成果(査定依頼や、来店予約)に結びつきやすいような工夫があれば嬉しいです。

【継続発注について】
まずはトップページのみのデザインをお願い致します。
トップページのデザインが決まりましたら、下層ページのデザインもお願いする予定です。(1ページ1~2万円程度の予定)
下層ページは2~3ページほどの予定ですので、総額12万円ぐらいの予定です。

【スマホ対応について】
コーディング時に、レスポンシブ対応する予定ですので、スマホ対応しやすいデザインにしていただければ助かります。

【レイアウトの変更などについて】
基本的にはワイヤーに沿って作っていただければと思います。
ただし、「もっとこうしたほうが良いのでは?」「こんな形はどうか?」といったようなご提案があれば、別途ご相談ください。

必要な資料は上記のzipファイルの中に入れておりますので、そちらをご覧ください。
もし不明な点があれば遠慮なくご連絡くださいませ。
1ページ
シンプル 複雑
単色 カラフル
暗い 明るい
日常 高級
遊び心 厳粛
未来的 伝統的
女性的 男性的
黄・オレンジ系
• 高解像度JPG (.jpg)
• イラストレーター形式 (.ai)
納品は、IllustratorでもPhotoshopでもFireworksでも、どのファイルでもOKです。

また、納品の際には使っているフォントをお教えください。
(使用フォントはモリサワ、もしくはフリーフォントでお願いします)
たくさんのご応募ありがとうございました。
非常に悩んだのですが、お一人の方を選ばせていただきました。
選に漏れた方々につきましては、お手数おかけしたにも関わらず何もお返しできずに心苦しくもあるのですが、ご了承いただければ幸いです。
またこれに懲りず、今後ともよろしくお願いいたします。
ありがとうございました!

いいデザインをしていただいた方が数人おられて、非常に悩みました。
その中で一番こちらの意図を汲み取っていただき、バランスの取れたデザインをしていただいた、ということで、こちらの方にお願いすることにしました。

たくさんのご応募ありがとうございました。
ありがとうございました!

```html
<!DOCTYPE html>
<html lang="ja">
<head>
<meta charset="utf-8">
<title>ソラミエ | 7階以上の高層階マンション買取サービス</title>
<link href="https://fonts.googleapis.com/css2?family=Noto+Sans+JP:wght@400;500;700;900&display=swap" rel="stylesheet">
<style>
:root{
  --orange:#f7923a;
  --orange-deep:#ee7a1e;
  --orange-pale:#fde3c6;
  --ink:#333333;
  --muted:#777777;
  --line:#dddddd;
  --blue:#3d8fd8;
  --dark:#3a3a3a;
  --white:#ffffff;
}
*{box-sizing:border-box;margin:0;padding:0}
html,body{width:1200px;height:3876px;overflow:hidden}
body{font-family:"Noto Sans JP",sans-serif;color:var(--ink);background:var(--white);font-size:14px;line-height:1.6}
section,header,footer,.block{overflow:hidden}
.brand{font-weight:900;letter-spacing:.08em;display:inline-flex;align-items:center;gap:10px}
.brand-mark{width:16px;height:16px;background:var(--orange);display:inline-block}

/* header */
.site-header{height:70px;display:flex;align-items:center;justify-content:space-between;padding:0 160px}
.site-header .brand{font-size:28px}
.header-tag{font-size:11px;color:var(--muted);line-height:1.4;margin-left:16px}
.header-nav{display:flex;gap:26px;font-size:12px;font-weight:700;align-items:center}
.header-nav small{display:block;font-size:10px;color:var(--muted);font-weight:400}
.header-nav .tel{color:var(--orange-deep);font-size:15px}

/* hero */
.hero{height:345px;position:relative;background:linear-gradient(180deg,#e9eef2 0%,#c9d2da 45%,#9aa4ad 100%)}
.hero-copy{position:absolute;right:220px;top:60px;text-align:center;color:var(--white);text-shadow:0 2px 6px rgba(0,0,0,.25)}
.hero-copy p{font-size:34px;font-weight:500;letter-spacing:.06em}
.hero-copy h1{font-size:42px;font-weight:900;letter-spacing:.06em}
.thumbs{height:85px;display:flex;align-items:center;justify-content:center;gap:14px}
.thumb{width:140px;height:60px;background:linear-gradient(135deg,#cfd6dc,#8d98a2)}
.thumb.active{outline:3px solid var(--orange)}
.arrow{width:24px;height:24px}

/* about */
.about{height:325px;text-align:center;padding-top:40px}
.section-title{font-size:30px;font-weight:900;line-height:1.4}
.section-title .brand{font-size:32px}
.about p{margin-top:26px;font-size:14px;line-height:2.1}

/* features */
.features{height:442px;background:var(--orange);padding-top:30px}
.feature-list{display:flex;justify-content:space-between;width:780px;margin:0 auto}
.feature{width:230px;text-align:center;color:var(--white)}
.feature-photo{width:180px;height:180px;border-radius:50%;margin:0 auto;border:5px solid var(--white)}
.feature-photo.a{background:linear-gradient(135deg,#f3f3f3,#bfc6cc)}
.feature-photo.b{background:linear-gradient(135deg,#f6e9e2,#d8b9a8)}
.feature-photo.c{background:linear-gradient(135deg,#eef1f4,#aab6c1)}
.feature h3{margin:-40px auto 0;position:relative;background:var(--white);color:var(--orange-deep);border-radius:50%;width:130px;height:70px;display:flex;align-items:center;justify-content:center;line-height:1.3;font-size:14px;font-weight:700}
.feature p{font-size:12px;margin-top:12px;line-height:1.7}
.btn-outline{display:flex;align-items:center;justify-content:center;gap:12px;width:400px;height:56px;margin:28px auto 0;border:2px solid var(--white);border-radius:4px;color:var(--white);font-size:20px;font-weight:700}

/* compare */
.compare{height:711px;padding-top:30px}
.compare .section-title{text-align:center}
.compare-box{margin:26px auto 0;width:900px;height:590px;border:4px solid var(--orange);display:flex}
.compare-col{flex:1;padding:22px 30px}
.compare-col.ours{background:var(--orange);color:var(--white)}
.compare-head{text-align:center;font-size:22px;font-weight:700;padding-bottom:12px;border-bottom:2px solid currentColor}
.others .compare-head{color:var(--orange-deep)}
.diagram{height:200px;margin:18px 0}
.others .diagram{background:linear-gradient(180deg,#fff4e8,#fde3c6)}
.ours .diagram{background:linear-gradient(180deg,#fbae6c,#f08a34)}
.compare-col h4{font-size:15px;font-weight:700;margin-top:14px;padding-left:14px;position:relative}
.compare-col h4::before{content:"";position:absolute;left:0;top:8px;width:8px;height:8px;background:currentColor}
.compare-col p{font-size:12px;line-height:1.8;margin-top:4px}
.ours .point{background:var(--white);color:var(--ink);padding:12px 16px;margin-top:14px}
.ours .point h4{margin-top:0;color:var(--orange-deep)}

/* faq */
.faq{height:672px;background:var(--orange);padding-top:34px}
.faq .section-title{text-align:center;color:var(--white)}
.faq-grid{display:grid;grid-template-columns:repeat(3,280px);gap:16px 20px;justify-content:center;margin-top:26px}
.faq-card{background:var(--white);height:258px;padding:16px}
.qa{display:flex;gap:10px}
.qa+.qa{margin-top:10px}
.badge{flex:none;width:32px;height:32px;border-radius:50%;color:var(--white);font-weight:900;display:flex;align-items:center;justify-content:center;font-size:18px}
.badge.q{background:var(--orange)}
.badge.a{background:var(--blue)}
.qa .question{font-size:13px;font-weight:700;line-height:1.5}
.qa .answer{font-size:11px;line-height:1.7;color:var(--muted)}

/* results */
.results{height:615px;padding-top:26px}
.results .section-title{text-align:center;padding-bottom:10px;border-bottom:1px solid var(--line);width:880px;margin:0 auto}
.result{display:flex;gap:30px;width:880px;margin:22px auto 0}
.result-photo{width:340px;height:232px;background:linear-gradient(180deg,#dde3e8,#7f8b95)}
.result-body{flex:1}
.result-body h3{font-size:16px;font-weight:700;line-height:1.5}
.result-meta{margin-top:10px;display:flex;gap:20px}
.result-meta ul{list-style:none;font-size:13px;width:150px}
.result-meta li{border-bottom:1px solid var(--line);padding:5px 0}
.result-meta li::before{content:"■";color:var(--orange);margin-right:6px;font-size:10px}
.result-note{flex:1;border:1px solid var(--orange);padding:10px 12px;font-size:11px;line-height:1.7;color:var(--muted)}
.btn-small{display:block;width:150px;margin:10px 0 0 auto;border:1px solid var(--orange);color:var(--orange-deep);text-align:center;font-size:12px;padding:4px 0}

.more{height:75px;text-align:center}
.btn-more{display:inline-block;width:420px;height:60px;line-height:60px;background:var(--orange);color:var(--white);font-size:21px;font-weight:700;border-radius:4px}

/* cta */
.cta{height:100px;display:flex;justify-content:center;align-items:center;gap:40px}
.cta a{width:390px;height:68px;border-radius:34px;display:flex;align-items:center;justify-content:center;color:var(--white);font-size:22px;font-weight:700}
.cta .assess{background:linear-gradient(180deg,#5aa7ea,var(--blue))}
.cta .visit{background:linear-gradient(180deg,#fb8f5a,#ec5f2c)}

/* footer */
.footer-brand{height:90px;text-align:center;padding-top:16px}
.footer-brand small{display:block;font-size:11px;color:var(--muted)}
.footer-brand .brand{font-size:28px}
.site-footer{background:var(--dark);color:#ddd;height:346px;padding-top:18px}
.footer-nav{display:flex;justify-content:center;gap:20px;font-size:11px;border-bottom:1px solid #555;padding-bottom:14px}
.footer-info{display:flex;width:900px;margin:26px auto 0;gap:30px;font-size:11px;line-height:1.8}
.footer-info strong{color:var(--white);font-size:14px}
.footer-text{width:260px}
.footer-photo{flex:1;height:190px;background:linear-gradient(180deg,#8a96a2,#4c5661)}
.copyright{text-align:center;font-size:10px;color:#999;margin-top:24px}
</style>
</head>
<body>

<header class="site-header">
  <div style="display:flex;align-items:center">
    <span class="brand"><span class="brand-mark"></span>ソラミエ</span>
    <span class="header-tag">7階以上の高層階<br>マンション買取サービス</span>
  </div>
  <nav class="header-nav">
    <span>ソラミエとは</span>
    <span><small>7階以上の高層階専門</small><span class="tel">0120-000-000</span></span>
    <span>買取実績</span>
    <span>店舗案内</span>
    <span><small>ご来店予約はこちら</small>来店予約</span>
  </nav>
</header>

<section class="hero" role="img" aria-label="高層マンションが立ち並ぶ都市の眺望写真">
  <div class="hero-copy">
    <p>マンション買取サービス</p>
    <h1>7階以上のお部屋、買取します。</h1>
  </div>
</section>

<div class="thumbs block">
  <svg class="arrow" viewBox="0 0 24 24"><path d="M15 4l-8 8 8 8" fill="none" stroke="#999" stroke-width="2"/></svg>
  <div class="thumb active" role="img" aria-label="都市の眺望"></div>
  <div class="thumb" role="img" aria-label="マンション外観"></div>
  <div class="thumb" role="img" aria-label="リビングの室内"></div>
  <div class="thumb" role="img" aria-label="高層ビル群"></div>
  <div class="thumb" role="img" aria-label="夜景"></div>
  <svg class="arrow" viewBox="0 0 24 24"><path d="M9 4l8 8-8 8" fill="none" stroke="#999" stroke-width="2"/></svg>
</div>

<section class="about">
  <h2 class="section-title"><span class="brand"><span class="brand-mark"></span>ソラミエ</span> とは?</h2>
  <p>「ソラミエ」は、7階以上の高層階専門のマンション買取サービスです。<br>
  眺望のよい高層階のお部屋を、専門スタッフが丁寧に査定し、スピーディーに買い取ります。<br>
  「ソラミエ」なら、仲介手数料は不要。安心してお住まいをお任せいただけます。</p>
</section>

<section class="features">
  <div class="feature-list">
    <div class="feature">
      <div class="feature-photo a" role="img" aria-label="電卓と書類の写真"></div>
      <h3>納得の金額を<br>ご提示します!</h3>
      <p>高層階ならではの価値を正しく評価し、相場に基づいた納得の金額をご提示します。</p>
    </div>
    <div class="feature">
      <div class="feature-photo b" role="img" aria-label="案内するスタッフの写真"></div>
      <h3>売買スムーズ!<br>すぐに現金化</h3>
      <p>当社が直接買い取るので、買い手を探す手間がなく、すぐに現金化できます。</p>
    </div>
    <div class="feature">
      <div class="feature-photo c" role="img" aria-label="住宅模型と書類の写真"></div>
      <h3>査定は無料!<br>手数料なし</h3>
      <p>査定は完全無料。仲介手数料もかからないため、余計な費用が発生しません。</p>
    </div>
  </div>
  <a class="btn-outline">ソラミエの詳細はこちら
    <svg width="18" height="18" viewBox="0 0 18 18"><path d="M6 3l6 6-6 6" fill="none" stroke="#fff" stroke-width="2"/></svg></a>
</section>

<section class="compare">
  <h2 class="section-title">一括見積サイトとの違い</h2>
  <div class="compare-box">
    <div class="compare-col others">
      <div class="compare-head">一括見積サイトとの違い</div>
      <div class="diagram" role="img" aria-label="一括見積サイトから複数の不動産会社へ個人情報が渡る仕組みのイラスト"></div>
      <h4>個人情報が拡散してしまう</h4>
      <p>個人情報が複数の会社に行き渡るため、電話やメールの営業が増え、対応に追われてしまいます。</p>
      <h4>当初の提示額どおりとは限らない</h4>
      <p>一括見積の金額は机上の概算であることが多く、訪問後に大きく下がることもあります。</p>
    </div>
    <div class="compare-col ours">
      <div class="compare-head">ソラミエの場合</div>
      <div class="diagram" role="img" aria-label="ソラミエとお客様が直接やり取りする仕組みのイラスト"></div>
      <div class="point">
        <h4>情報漏れの心配がありません</h4>
        <p>当社だけでやり取りが完結するため、個人情報が他社へ渡ることはありません。</p>
      </div>
      <div class="point">
        <h4>提示額でそのまま買取</h4>
        <p>専門スタッフが現地で正確に査定し、ご提示した金額でそのまま買い取ります。</p>
      </div>
    </div>
  </div>
</section>

<section class="faq">
  <h2 class="section-title">よくある質問</h2>
  <div class="faq-grid">
    <div class="faq-card">
      <div class="qa"><span class="badge q">Q</span><p class="question">査定にはどのくらい時間がかかりますか?</p></div>
      <div class="qa"><span class="badge a">A</span><p class="answer">お部屋を拝見してから、通常は当日から数日以内に査定結果をお伝えしています。お急ぎの場合はお気軽にご相談ください。</p></div>
    </div>
    <div class="faq-card">
      <div class="qa"><span class="badge q">Q</span><p class="question">住宅ローンが残っていても売れますか?</p></div>
      <div class="qa"><span class="badge a">A</span><p class="answer">はい、可能です。売却代金でローンを完済する方法など、状況に合わせた進め方を専門スタッフがご案内いたします。</p></div>
    </div>
    <div class="faq-card">
      <div class="qa"><span class="badge q">Q</span><p class="question">住みながら査定を受けられますか?</p></div>
      <div class="qa"><span class="badge a">A</span><p class="answer">もちろん可能です。お住まいのままで査定いたしますので、事前の片付けや準備も最小限で問題ありません。</p></div>
    </div>
    <div class="faq-card">
      <div class="qa"><span class="badge q">Q</span><p class="question">査定後に断っても費用はかかりませんか?</p></div>
      <div class="qa"><span class="badge a">A</span><p class="answer">査定は無料です。金額にご納得いただけない場合はお断りいただいても、費用は一切かかりません。</p></div>
    </div>
    <div class="faq-card">
      <div class="qa"><span class="badge q">Q</span><p class="question">6階以下のお部屋は対象外ですか?</p></div>
      <div class="qa"><span class="badge a">A</span><p class="answer">当サービスは7階以上の高層階専門です。それ以下の階のお部屋についても、まずはご相談ください。</p></div>
    </div>
    <div class="faq-card">
      <div class="qa"><span class="badge q">Q</span><p class="question">引き渡しの時期は相談できますか?</p></div>
      <div class="qa"><span class="badge a">A</span><p class="answer">はい、新居へのお引越し時期などに合わせて、引き渡し日を柔軟に調整させていただきます。</p></div>
    </div>
  </div>
</section>

<section class="results">
  <h2 class="section-title">買取実績</h2>
  <article class="result">
    <div class="result-photo" role="img" aria-label="高層マンションの外観写真"></div>
    <div class="result-body">
      <h3>湾岸エリア 高層タワーマンション 18階<br>眺望良好な3LDKのお部屋</h3>
      <div class="result-meta">
        <ul><li>エリア:港区</li><li>買取額:3,980万円</li><li>階数:18階</li><li>時期:4月</li></ul>
        <div class="result-note">眺望の良さを評価し、ご希望に近い金額でお買取りしました。スピーディーな対応にご満足いただけました。ご相談から約2週間で、お引き渡しまで完了しています。</div>
      </div>
      <a class="btn-small">詳しくみる ›</a>
    </div>
  </article>
  <article class="result">
    <div class="result-photo" role="img" aria-label="高層マンションの外観写真"></div>
    <div class="result-body">
      <h3>駅徒歩5分 駅近高層マンション 12階<br>南向きの2LDKのお部屋</h3>
      <div class="result-meta">
        <ul><li>エリア:品川区</li><li>買取額:3,500万円</li><li>階数:12階</li><li>時期:6月</li></ul>
        <div class="result-note">住み替えのご予定に合わせて、引き渡し時期を調整しました。住みながらの査定で、準備の負担も少なく進められました。手数料がかからない点もご好評でした。</div>
      </div>
      <a class="btn-small">詳しくみる ›</a>
    </div>
  </article>
</section>

<div class="more block"><a class="btn-more">買取実績をもっとみる ›</a></div>

<div class="cta block">
  <a class="assess">買取無料査定はこちら ›</a>
  <a class="visit">ご来店予約はこちら ›</a>
</div>

<div class="footer-brand block">
  <small>7階以上の高層階マンション買取サービス</small>
  <span class="brand"><span class="brand-mark"></span>ソラミエ</span>
</div>

<footer class="site-footer">
  <nav class="footer-nav">
    <span>トップページ</span><span>ソラミエとは</span><span>買取実績</span><span>よくある質問</span><span>店舗案内</span><span>無料査定</span><span>来店予約</span><span>会社概要</span><span>プライバシーポリシー</span>
  </nav>
  <div class="footer-info">
    <div class="footer-text"><strong>運営:株式会社ソラミエリアルティ</strong><br>〒100-0000<br>東京都中央区サンプル町1-2-3<br>TEL:0120-000-000<br>営業時間 10:00〜19:00</div>
    <div class="footer-text">高層階マンションの買取を専門に行う不動産会社です。宅地建物取引業免許を取得し、安心のお取引をお約束いたします。査定やご来店のご予約は、お電話またはフォームからお気軽にどうぞ。</div>
    <div class="footer-photo" role="img" aria-label="高層ビルが並ぶ街並みの写真"></div>
  </div>
  <p class="copyright">Copyright © ソラミエ All Rights Reserved.</p>
</footer>

</body>
</html>
```